Ruler design for Brodmere Liquid waste

We require a very professional design for our marketing product 'Ruler'.
It will be on a white plastic ruler 315mm long and 39mm high.
0 – 30 on the top (in mm).
0 – 12 on the bottom (in inches).
Numbering in black (to be included as an example only) as it is already printed on the plastic stock.
I want logo, phone number, email and website.
Phone number - 08 8317 4925, email info@bwx.com.au, web www.brodmereliquidwaste.com
Large text - Your Local Grease Trap and Liquid Waste Specialists
Please stick to our colours.
Total workable text area –
Length 312mm
Height 24mm
You must supply Print ready pdf files with
all fonts embedded.
Please include crop marks plus 3mm bleed all round.
Marketing

```html
<!DOCTYPE html>
<html lang="en">
<head>
<meta charset="utf-8">
<title>Brodmere Liquid Waste – Ruler</title>
<link href="https://fonts.googleapis.com/css2?family=Arimo:wght@400;700&family=Delius&display=swap" rel="stylesheet">
<style>
  :root {
    --paper: #ffffff;
    --ink: #1a1a1a;
    --scale-grey: #555555;
    --brand-orange: #f26522;
    --brand-navy: #0c1f5c;
    --brand-yellow: #ffd200;
  }
  html, body {
    margin: 0;
    padding: 0;
    overflow: hidden;
    background: var(--paper);
  }
  .ruler {
    position: relative;
    width: 1200px;
    height: 170px;
    background: var(--paper);
    overflow: hidden;
    font-family: "Arimo", Arial, sans-serif;
  }
  .ruler__graphics {
    position: absolute;
    inset: 0;
  }
  .scale-number {
    font-family: "Arimo", Arial, sans-serif;
    font-size: 11px;
    fill: var(--ink);
  }
  .arc {
    fill: none;
    stroke: var(--brand-orange);
  }
  .brand-block {
    position: absolute;
    left: 82px;
    top: 35px;
    width: 145px;
    height: 96px;
    background: var(--brand-navy);
    display: flex;
    align-items: center;
    justify-content: center;
    text-align: center;
  }
  .brand-block__name {
    font-family: "Arimo", Arial, sans-serif;
    font-weight: 700;
    font-size: 15px;
    line-height: 1.15;
    color: var(--brand-yellow);
    letter-spacing: 0.5px;
    text-transform: uppercase;
  }
  .tagline {
    position: absolute;
    left: 677px;
    top: 50px;
    width: 523px;
    height: 31px;
    background: var(--brand-orange);
    color: var(--paper);
    font-family: "Delius", "Comic Sans MS", cursive;
    font-size: 19px;
    line-height: 31px;
    padding-left: 10px;
    box-sizing: border-box;
    white-space: nowrap;
  }
  .contacts {
    position: absolute;
    top: 108px;
    left: 0;
    height: 20px;
    width: 100%;
  }
  .contact {
    position: absolute;
    top: 0;
    display: flex;
    align-items: center;
    gap: 8px;
    font-size: 13.5px;
    color: var(--ink);
    white-space: nowrap;
  }
  .contact svg {
    width: 17px;
    height: 17px;
    flex: none;
  }
  .contact--phone { left: 241px; }
  .contact--email { left: 382px; }
  .contact--web { left: 553px; }
</style>
</head>
<body>
<div class="ruler">
  <svg class="ruler__graphics" width="1200" height="170" viewBox="0 0 1200 170" xmlns="http://www.w3.org/2000/svg">
    <defs>
      <pattern id="mm-ticks" patternUnits="userSpaceOnUse" x="40" y="0" width="3.7333" height="170">
        <rect x="0" y="0" width="0.8" height="6" fill="var(--scale-grey)"/>
      </pattern>
      <pattern id="half-cm-ticks" patternUnits="userSpaceOnUse" x="40" y="0" width="18.6667" height="170">
        <rect x="0" y="0" width="0.9" height="10" fill="var(--scale-grey)"/>
      </pattern>
      <pattern id="cm-ticks" patternUnits="userSpaceOnUse" x="40" y="0" width="37.3333" height="170">
        <rect x="0" y="0" width="1" height="14" fill="var(--ink)"/>
      </pattern>
      <pattern id="sixteenth-ticks" patternUnits="userSpaceOnUse" x="1162" y="0" width="5.9010" height="170">
        <rect x="0" y="166" width="0.8" height="4" fill="var(--scale-grey)"/>
      </pattern>
      <pattern id="eighth-ticks" patternUnits="userSpaceOnUse" x="1162" y="0" width="11.8021" height="170">
        <rect x="0" y="164" width="0.8" height="6" fill="var(--scale-grey)"/>
      </pattern>
      <pattern id="quarter-ticks" patternUnits="userSpaceOnUse" x="1162" y="0" width="23.6042" height="170">
        <rect x="0" y="161" width="0.9" height="9" fill="var(--scale-grey)"/>
      </pattern>
      <pattern id="half-inch-ticks" patternUnits="userSpaceOnUse" x="1162" y="0" width="47.2083" height="170">
        <rect x="0" y="158" width="0.9" height="12" fill="var(--scale-grey)"/>
      </pattern>
      <pattern id="inch-ticks" patternUnits="userSpaceOnUse" x="1162" y="0" width="94.4167" height="170">
        <rect x="0" y="154" width="1" height="16" fill="var(--ink)"/>
      </pattern>
    </defs>

    <!-- decorative arcs -->
    <g class="arcs">
      <circle class="arc" cx="448" cy="52" r="63" stroke-width="4"/>
      <circle class="arc" cx="300" cy="210" r="92" stroke-width="9"/>
      <circle class="arc" cx="248" cy="170" r="78" stroke-width="6"/>
    </g>

    <!-- metric scale -->
    <g class="scale scale--metric">
      <rect x="39" y="0" width="1123" height="16" fill="url(#mm-ticks)"/>
      <rect x="39" y="0" width="1123" height="16" fill="url(#half-cm-ticks)"/>
      <rect x="39" y="0" width="1123" height="16" fill="url(#cm-ticks)"/>
      <text class="scale-number" x="33" y="26">0<tspan font-size="7" dx="3">mm</tspan></text>
      <text class="scale-number" x="77.3" y="26" text-anchor="middle">1</text>
      <text class="scale-number" x="114.7" y="26" text-anchor="middle">2</text>
      <text class="scale-number" x="152" y="26" text-anchor="middle">3</text>
      <text class="scale-number" x="189.3" y="26" text-anchor="middle">4</text>
      <text class="scale-number" x="226.7" y="26" text-anchor="middle">5</text>
      <text class="scale-number" x="264" y="26" text-anchor="middle">6</text>
      <text class="scale-number" x="301.3" y="26" text-anchor="middle">7</text>
      <text class="scale-number" x="338.7" y="26" text-anchor="middle">8</text>
      <text class="scale-number" x="376" y="26" text-anchor="middle">9</text>
      <text class="scale-number" x="413.3" y="26" text-anchor="middle">10</text>
      <text class="scale-number" x="450.7" y="26" text-anchor="middle">11</text>
      <text class="scale-number" x="488" y="26" text-anchor="middle">12</text>
      <text class="scale-number" x="525.3" y="26" text-anchor="middle">13</text>
      <text class="scale-number" x="562.7" y="26" text-anchor="middle">14</text>
      <text class="scale-number" x="600" y="26" text-anchor="middle">15</text>
      <text class="scale-number" x="637.3" y="26" text-anchor="middle">16</text>
      <text class="scale-number" x="674.7" y="26" text-anchor="middle">17</text>
      <text class="scale-number" x="712" y="26" text-anchor="middle">18</text>
      <text class="scale-number" x="749.3" y="26" text-anchor="middle">19</text>
      <text class="scale-number" x="786.7" y="26" text-anchor="middle">20</text>
      <text class="scale-number" x="824" y="26" text-anchor="middle">21</text>
      <text class="scale-number" x="861.3" y="26" text-anchor="middle">22</text>
      <text class="scale-number" x="898.7" y="26" text-anchor="middle">23</text>
      <text class="scale-number" x="936" y="26" text-anchor="middle">24</text>
      <text class="scale-number" x="973.3" y="26" text-anchor="middle">25</text>
      <text class="scale-number" x="1010.7" y="26" text-anchor="middle">26</text>
      <text class="scale-number" x="1048" y="26" text-anchor="middle">27</text>
      <text class="scale-number" x="1085.3" y="26" text-anchor="middle">28</text>
      <text class="scale-number" x="1122.7" y="26" text-anchor="middle">29</text>
      <text class="scale-number" x="1160" y="26" text-anchor="middle">30</text>
    </g>

    <!-- imperial scale (reads upside down) -->
    <g class="scale scale--imperial">
      <rect x="28" y="150" width="1136" height="20" fill="url(#sixteenth-ticks)"/>
      <rect x="28" y="150" width="1136" height="20" fill="url(#eighth-ticks)"/>
      <rect x="28" y="150" width="1136" height="20" fill="url(#quarter-ticks)"/>
      <rect x="28" y="150" width="1136" height="20" fill="url(#half-inch-ticks)"/>
      <rect x="28" y="150" width="1136" height="20" fill="url(#inch-ticks)"/>
      <text class="scale-number" transform="rotate(180 1168 140)" x="1168" y="140">0<tspan font-size="7" dx="3">inch</tspan></text>
      <text class="scale-number" transform="rotate(180 1067.6 140)" x="1067.6" y="140" text-anchor="middle">1</text>
      <text class="scale-number" transform="rotate(180 973.2 140)" x="973.2" y="140" text-anchor="middle">2</text>
      <text class="scale-number" transform="rotate(180 878.8 140)" x="878.8" y="140" text-anchor="middle">3</text>
      <text class="scale-number" transform="rotate(180 784.3 140)" x="784.3" y="140" text-anchor="middle">4</text>
      <text class="scale-number" transform="rotate(180 689.9 140)" x="689.9" y="140" text-anchor="middle">5</text>
      <text class="scale-number" transform="rotate(180 595.5 140)" x="595.5" y="140" text-anchor="middle">6</text>
      <text class="scale-number" transform="rotate(180 501.1 140)" x="501.1" y="140" text-anchor="middle">7</text>
      <text class="scale-number" transform="rotate(180 406.7 140)" x="406.7" y="140" text-anchor="middle">8</text>
      <text class="scale-number" transform="rotate(180 312.3 140)" x="312.3" y="140" text-anchor="middle">9</text>
      <text class="scale-number" transform="rotate(180 217.8 140)" x="217.8" y="140" text-anchor="middle">10</text>
      <text class="scale-number" transform="rotate(180 123.4 140)" x="123.4" y="140" text-anchor="middle">11</text>
      <text class="scale-number" transform="rotate(180 29 140)" x="29" y="140" text-anchor="middle">12</text>
    </g>
  </svg>

  <div class="brand-block">
    <span class="brand-block__name">Brodmere<br>Liquid Waste</span>
  </div>

  <div class="tagline">Your Local Grease Trap and Liquid Waste Specialists</div>

  <div class="contacts">
    <div class="contact contact--phone">
      <svg viewBox="0 0 24 24" aria-hidden="true"><path fill="#222" d="M3 9c0-3 4-5 9-5s9 2 9 5v2h-5V9c0-1-2-1.5-4-1.5S8 8 8 9v2H3zM6 13h12l2 7H4z"/><circle cx="12" cy="16.5" r="2" fill="#fff"/></svg>
      <span>08 8317 4925</span>
    </div>
    <div class="contact contact--email">
      <svg viewBox="0 0 24 24" aria-hidden="true"><rect x="2" y="5" width="20" height="14" fill="#222"/><path d="M3 6l9 7 9-7" fill="none" stroke="#fff" stroke-width="1.6"/></svg>
      <span>info@bwx.com.au</span>
    </div>
    <div class="contact contact--web">
      <svg viewBox="0 0 24 24" aria-hidden="true"><g fill="none" stroke="#222" stroke-width="1.6"><circle cx="12" cy="12" r="9.5"/><ellipse cx="12" cy="12" rx="4.2" ry="9.5"/><path d="M2.5 12h19M4 7h16M4 17h16"/></g></svg>
      <span>www.brodmereliquidwaste.com</span>
    </div>
  </div>
</div>
</body>
</html>
```